Expedition Cruise Sales Website for the Polar Regions (Antarctica & Arctic)

This will be a website for selling cruises.
This site should have a homepage, a ship page, destinations, and itineraries.
I have created a file specifying each page, and it is attached.
Pages:
1. Home
2. Cruise Lines
- 2.1 Ships
3. Destinations
- 3.1 Region - 3.2 Country - 3.3 City
4. Itineraries
- 4.1 Itinerary
5. Blog / Travel Tips 6. About Us
7. Contact
Please take a look on the attached pdf
Target Market(s)
Expedition Travelers
Coding
Coded - Design and coding required
Number of Pages Required
5+ page
Font styles to use
Look and feel
Each slider illustrates characteristics of the customer's brand and the style your logo design should communicate.

```html
<!DOCTYPE html>
<html lang="en">
<head>
<meta charset="utf-8">
<title>Glacia Voyages — Polar Expedition Cruises</title>
<link rel="stylesheet" href="https://fonts.googleapis.com/css2?family=Jost:wght@400;500;600;700&family=Great+Vibes&display=swap">
<style>
:root{
  --page:#f3f3f3;
  --brand:#3e6fae;
  --navy:#1f3350;
  --slate:#4d6890;
  --slate-dark:#3f5878;
  --ink:#333a44;
  --muted:#6b7380;
  --white:#ffffff;
  --gold:#f7e66a;
  --ice-1:#c9d3dc;
  --ice-2:#6c8298;
}
*{box-sizing:border-box;margin:0;padding:0}
html,body{width:1200px;height:3906px;overflow:hidden}
body{position:relative;background:var(--white);font-family:"Jost",sans-serif;color:var(--ink)}
.abs{position:absolute}

/* header */
.site-header{left:0;top:0;width:1200px;height:290px;background:var(--page)}
.brand{left:0;width:1200px;top:70px;text-align:center}
.brand-mark{display:inline-block;width:46px;height:46px;border-radius:50%;background:var(--brand)}
.brand-name{display:block;margin-top:8px;font-size:44px;font-weight:600;color:var(--brand);letter-spacing:.5px}
.header-icons{right:80px;top:106px;display:flex;gap:34px}
.main-nav{left:40px;width:1120px;top:238px;display:flex;justify-content:space-between;font-size:17px;color:var(--brand);letter-spacing:.3px}
.main-nav .sep{color:var(--brand)}
.main-nav .current{color:var(--navy);text-decoration:underline;text-underline-offset:5px}

/* hero */
.hero{left:0;top:290px;width:1200px;height:620px;background:linear-gradient(180deg,#9aa9b8 0%,#d7dde3 30%,#7e94a8 55%,#2d3f55 100%)}
.hero-eyebrow{left:152px;top:382px;font-size:16px;color:var(--white);letter-spacing:.5px}
.hero-title{left:152px;top:408px;font-size:39px;font-weight:600;color:var(--white);letter-spacing:.5px}
.search-panel{left:153px;top:482px;width:894px;height:235px;background:rgba(235,238,242,.72)}
.field-label{font-size:15px;font-weight:600;color:var(--ink)}
.field{height:30px;border-radius:15px;background:rgba(255,255,255,.75);font-size:12px;color:var(--muted);padding:7px 16px;display:flex;justify-content:space-between;align-items:center}
.price-track{height:3px;background:#5b6270}
.price-knob{width:10px;height:10px;border-radius:50%;background:var(--navy)}

/* best deal */
.section-title{left:0;width:1200px;text-align:center;font-weight:600;letter-spacing:.5px}
.best-title{top:975px;font-size:32px;color:var(--slate-dark)}
.deal-card{top:1082px;width:351px;height:340px;overflow:hidden}
.deal-photo{position:absolute;inset:0}
.deal-card .shade{position:absolute;left:0;right:0;bottom:0;height:120px;background:linear-gradient(180deg,rgba(0,0,0,0),rgba(0,0,0,.7))}
.deal-name{position:absolute;left:15px;bottom:52px;font-size:22px;font-weight:600;color:var(--white)}
.deal-nights{position:absolute;left:17px;bottom:36px;font-size:11px;color:var(--white)}
.deal-rating{position:absolute;left:17px;bottom:12px;display:flex;align-items:center;gap:10px;color:var(--white);font-size:10px}
.deal-rating u{color:var(--gold)}
.deal-price{position:absolute;right:10px;bottom:4px;font-size:33px;font-weight:700;color:var(--gold)}
.slider-dot{top:1488px;width:12px;height:12px;border-radius:50%;background:var(--slate-dark)}

.feature-card{top:1564px;width:573px;height:557px;overflow:hidden}
.feature-card .shade{position:absolute;left:0;right:0;bottom:0;height:200px;background:linear-gradient(180deg,rgba(20,35,60,0),rgba(20,35,60,.9))}
.btn-light{display:inline-block;background:var(--white);color:var(--navy);font-size:10px;font-weight:700;padding:5px 20px;letter-spacing:.3px}
.feature-text{font-size:12.5px;color:var(--white);line-height:1.5}

/* testimonials */
.testimonials{left:0;top:2224px;width:1200px;height:813px;background:var(--slate)}
.say-title{top:2283px;font-size:33px;color:var(--white)}
.review-card{top:2470px;width:461px;height:514px;background:linear-gradient(180deg,#fafafa,#e4e6e9);text-align:center}
.avatar{width:228px;height:228px;border-radius:50%;background:var(--white);box-shadow:0 6px 10px rgba(0,0,0,.35);padding:8px}
.avatar span{display:block;width:100%;height:100%;border-radius:50%;border:5px solid var(--slate)}
.review-name{font-size:21px;font-weight:600;color:var(--ink);margin-top:165px}
.review-role{font-size:13px;font-weight:500;color:var(--ink);margin-top:2px}
.review-stars{margin-top:8px;display:flex;justify-content:center;gap:6px}
.review-text{font-size:12.5px;line-height:1.45;color:var(--ink);margin-top:62px}
.quote{position:absolute;font-size:110px;font-weight:700;color:#b4bdca;line-height:1}
.round-arrow{width:38px;height:38px;border-radius:50%;background:#e8eaee;display:flex;align-items:center;justify-content:center;color:var(--slate);font-size:20px;font-weight:600}

/* newsletter */
.newsletter{left:0;top:3102px;width:1200px;height:398px;background:linear-gradient(180deg,#3c4658 0%,#6d6a6c 45%,#2c2d34 100%)}
.newsletter-box{left:262px;top:3171px;width:675px;height:257px;background:rgba(220,224,232,.82)}
.newsletter-title{font-size:26px;font-weight:600;color:var(--slate-dark);text-align:center;margin-top:28px}
.btn-dark{background:var(--slate-dark);color:var(--white);font-size:10px;padding:7px 20px;letter-spacing:.3px}

/* footer */
.site-footer{left:0;top:3500px;width:1200px;height:292px;background:var(--slate);color:var(--white)}
.foot-head{font-size:13px;font-weight:600;letter-spacing:.3px}
.foot-list{list-style:none;font-size:13px;line-height:30px;margin-top:22px}
.social{display:flex;gap:25px;margin-top:24px}
.social span{width:22px;height:22px;border-radius:50%;border:2px solid var(--white)}
</style>
</head>
<body>

<header class="site-header abs">
  <div class="brand abs">
    <span class="brand-mark"></span>
    <span class="brand-name">Glacia Voyages</span>
  </div>
  <div class="header-icons abs">
    <svg width="22" height="22" viewBox="0 0 22 22" fill="none" stroke="#3e6fae" stroke-width="1.6"><circle cx="11" cy="11" r="9.5"/><circle cx="11" cy="9" r="3.5"/><path d="M4.5 17.5c2-3 11-3 13 0"/></svg>
    <svg width="26" height="22" viewBox="0 0 26 22" fill="none" stroke="#3e6fae" stroke-width="1.6"><path d="M1 2h4l3 13h13l3-9H7"/><circle cx="10" cy="19" r="1.6"/><circle cx="19" cy="19" r="1.6"/></svg>
    <svg width="22" height="22" viewBox="0 0 22 22" fill="none" stroke="#3e6fae" stroke-width="1.8"><circle cx="9" cy="9" r="7"/><path d="M14 14l6 6"/></svg>
  </div>
  <nav class="main-nav abs">
    <span class="current">HOME</span><span class="sep">|</span>
    <span>CRUISE LINES</span><span class="sep">|</span>
    <span>DESTINATIONS</span><span class="sep">|</span>
    <span>ITINERARIES</span><span class="sep">|</span>
    <span>BLOG / TRAVEL TIPS</span><span class="sep">|</span>
    <span>ABOUT US</span><span class="sep">|</span>
    <span>CONTACT</span>
  </nav>
</header>

<section class="hero abs" role="img" aria-label="Photo of snowy Antarctic mountains reflected in calm water, seen from a ship's bow"></section>
<div class="hero-eyebrow abs">OUR PACKAGE</div>
<h1 class="hero-title abs">SEARCH YOUR HOLIDAY</h1>
<form class="search-panel abs">
  <div class="abs" style="left:26px;top:82px;width:240px">
    <div class="field-label">Select Your Destination :</div>
    <div class="field" style="margin-top:12px">All Destination
      <svg width="12" height="15" viewBox="0 0 12 15" fill="none" stroke="#8a909a" stroke-width="1.3"><path d="M6 14s5-5 5-8.5A5 5 0 0 0 1 5.5C1 9 6 14 6 14z"/><circle cx="6" cy="5.5" r="1.8"/></svg>
    </div>
  </div>
  <div class="abs" style="left:310px;top:82px;width:240px">
    <div class="field-label">Select Your Date :</div>
    <div class="field" style="margin-top:12px">mm-dd-yyyy
      <svg width="15" height="14" viewBox="0 0 15 14" fill="none" stroke="#8a909a" stroke-width="1.2"><rect x="1" y="2" width="13" height="11"/><path d="M1 5h13M4 0v3M11 0v3M4 8h2M9 8h2M4 11h2M9 11h2"/></svg>
    </div>
  </div>
  <div class="abs" style="left:607px;top:82px;width:260px">
    <div class="field-label" style="display:flex;justify-content:space-between"><span>Max Price :</span><span>$ 5000</span></div>
    <div class="abs price-track" style="left:0;top:34px;width:260px"></div>
    <div class="abs price-knob" style="left:132px;top:30px"></div>
    <div class="abs" style="left:0;top:50px;display:flex;align-items:center;gap:9px;font-size:12px;font-weight:500;color:#4a505a">
      <span style="width:11px;height:11px;background:rgba(255,255,255,.8)"></span>See only promotions
    </div>
  </div>
</form>

<h2 class="section-title best-title abs">BEST DEAL</h2>
<svg class="abs" style="left:18px;top:1234px" width="18" height="28" viewBox="0 0 18 28" fill="none" stroke="#3f5878" stroke-width="3.5"><path d="M15 2L4 14l11 12"/></svg>
<svg class="abs" style="left:1156px;top:1234px" width="18" height="28" viewBox="0 0 18 28" fill="none" stroke="#3f5878" stroke-width="3.5"><path d="M3 2l11 12L3 26"/></svg>

<article class="deal-card abs" style="left:62px">
  <div class="deal-photo" role="img" aria-label="Photo of a cruise yacht beside rocky cliffs at sunset" style="background:linear-gradient(180deg,#4f7fb0 0%,#8aa8c4 35%,#b07a46 55%,#243a58 80%)"></div>
  <div class="shade"></div>
  <div class="deal-name">TOP GALÁPAGOS CRUISES</div>
  <div class="deal-nights">18 Nights Tour</div>
  <div class="deal-rating"><span style="font-size:15px;letter-spacing:1px">★★★★☆</span><u>9 Reviews</u></div>
  <div class="deal-price">$1234</div>
</article>
<article class="deal-card abs" style="left:423px">
  <div class="deal-photo" role="img" aria-label="Photo of a cruise ship before snowy mountains under blue sky" style="background:linear-gradient(180deg,#1f63b4 0%,#7fa6d2 30%,#dfe6ee 48%,#2f6aa5 62%,#153a66 100%)"></div>
  <div class="shade"></div>
  <div class="deal-name">BEST ANTARCTIC CRUISES</div>
  <div class="deal-nights">14 Nights Tour</div>
  <div class="deal-rating"><span style="font-size:15px;letter-spacing:1px">★★★★☆</span><u>9 Reviews</u></div>
  <div class="deal-price">$1234</div>
</article>
<article class="deal-card abs" style="left:783px">
  <div class="deal-photo" role="img" aria-label="Photo of an expedition ship among icy peaks" style="background:linear-gradient(180deg,#6f9bd0 0%,#c9d6e4 35%,#5f748c 55%,#23364f 100%)"></div>
  <div class="shade"></div>
  <div class="deal-name">LAST-MINUTE DEALS</div>
  <div class="deal-nights">9 Nights Tour</div>
  <div class="deal-rating"><span style="font-size:15px;letter-spacing:1px">★★★★☆</span><u>9 Reviews</u></div>
  <div class="deal-price">$1234</div>
</article>

<span class="slider-dot abs" style="left:481px"></span>
<span class="slider-dot abs" style="left:526px"></span>
<span class="slider-dot abs" style="left:571px"></span>
<span class="slider-dot abs" style="left:616px"></span>
<span class="slider-dot abs" style="left:661px"></span>
<span class="slider-dot abs" style="left:706px"></span>

<article class="feature-card abs" style="left:21px">
  <div class="deal-photo" role="img" aria-label="Photo of two travellers in red jackets walking across a snowy Antarctic shore" style="background:linear-gradient(180deg,#aab3c4 0%,#cfd5de 45%,#eef0f3 62%,#c8ccd4 75%)"></div>
  <div class="shade"></div>
  <div class="abs" style="left:0;width:573px;top:402px;text-align:center;color:#fff">
    <div style="font-size:12px;font-weight:500;letter-spacing:.5px">BEST DESTINATION</div>
    <div style="font-family:'Great Vibes',cursive;font-size:40px;line-height:1.1">South Shetland Islands</div>
    <p class="feature-text" style="margin-top:8px">Lorem Ipsum is simply dummy text of the printing<br>and typesetting industry. Lorem Ipsum has been the industry's standard</p>
    <span class="btn-light" style="margin-top:10px">SEE DETAILS</span>
  </div>
</article>
<article class="feature-card abs" style="left:604px">
  <div class="deal-photo" role="img" aria-label="Photo of a cruise ship docked before curved high-rise towers" style="background:linear-gradient(180deg,#4f74a6 0%,#a7bad0 35%,#8f9cad 60%,#2c415e 100%)"></div>
  <div class="shade"></div>
  <div class="abs" style="left:27px;top:424px;color:#fff;width:520px">
    <div style="font-size:27px;font-weight:600;letter-spacing:.3px">CRUISE END YEAR PACKAGE</div>
    <p class="feature-text" style="margin-top:2px">Lorem Ipsum is simply dummy text of the printing<br>and typesetting industry. Lorem Ipsum has been the industry's standard</p>
    <div style="margin-top:8px;display:flex;align-items:center;gap:10px;font-size:10px"><span style="font-size:16px">★★★★☆</span><u style="color:var(--gold)">9 Reviews</u></div>
  </div>
  <span class="btn-light abs" style="right:28px;top:533px">SEE DETAILS</span>
</article>

<section class="testimonials abs"></section>
<h2 class="section-title say-title abs">WHAT THEY SAY</h2>
<div class="round-arrow abs" style="left:73px;top:2721px">&lt;</div>
<div class="round-arrow abs" style="left:1108px;top:2721px">&gt;</div>

<article class="review-card abs" style="left:138px">
  <div class="avatar abs" style="left:116px;top:-135px"><span role="img" aria-label="Portrait photo of Mr. Ipsum" style="background:linear-gradient(180deg,#d9dde2,#7f8a98)"></span></div>
  <div class="review-name">Mr. Ipsum</div>
  <div class="review-role">General Manager</div>
  <div class="review-stars" style="font-size:34px;color:var(--slate-dark);line-height:1">★★★★★</div>
  <span class="quote" style="left:45px;top:230px">“</span>
  <p class="review-text">Lorem ipsum dolor sit amet, consectetur adipiscing elit.<br>Maecenas ornare non leo sed tempor.<br>Quisque tincidunt, magna nec porttitor varius,<br>odio erat porta velit, eu fermentum neque risus id nisi.<br>Fusce eu volutpat odio.<br>Pellentesque habitant morbi tristique senectus<br>et netus et malesuada fames ac turpis egestas.</p>
  <span class="quote" style="right:50px;top:428px">”</span>
</article>
<article class="review-card abs" style="left:623px">
  <div class="avatar abs" style="left:116px;top:-135px"><span role="img" aria-label="Portrait photo of Mrs. Lorem" style="background:linear-gradient(180deg,#b9a796,#3b3535)"></span></div>
  <div class="review-name">Mrs. Lorem</div>
  <div class="review-role">Accounting</div>
  <div class="review-stars" style="font-size:34px;color:var(--slate-dark);line-height:1">★★★★★</div>
  <span class="quote" style="left:45px;top:230px">“</span>
  <p class="review-text">Lorem ipsum dolor sit amet, consectetur adipiscing elit.<br>Maecenas ornare non leo sed tempor.<br>Quisque tincidunt, magna nec porttitor varius,<br>odio erat porta velit, eu fermentum neque risus id nisi.<br>Fusce eu volutpat odio.<br>Pellentesque habitant morbi tristique senectus<br>et netus et malesuada fames ac turpis egestas.</p>
  <span class="quote" style="right:50px;top:428px">”</span>
</article>

<section class="newsletter abs" role="img" aria-label="Photo of polar mountains glowing at sunset over still water"></section>
<form class="newsletter-box abs">
  <div class="newsletter-title">NEWSLETTER</div>
  <p class="abs" style="left:223px;top:94px;font-size:12.5px;line-height:1.35;color:var(--ink)">Sign up for exclusive offer, original<br>stories, events and more</p>
  <div class="abs" style="left:223px;top:136px;width:230px;height:31px;background:#fff;font-size:9px;color:#8a909a;padding:10px 11px">Enter Email</div>
  <span class="btn-dark abs" style="left:299px;top:191px">SIGN UP</span>
</form>

<footer class="site-footer abs">
  <div class="abs" style="left:94px;top:57px">
    <div class="foot-head">TRAVEL SPECIALIST</div>
    <ul class="foot-list"><li>First Class Ticket</li><li>Accessible Travel</li><li>Amazing Cruise</li><li>Cruise VIP</li></ul>
  </div>
  <div class="abs" style="left:366px;top:57px">
    <div class="foot-head">COMPANY INFORMATION</div>
    <ul class="foot-list"><li>About Us</li><li>Our Crew</li><li>Services</li><li>Cruise</li><li>Destinations</li></ul>
  </div>
  <div class="abs" style="left:652px;top:57px">
    <div class="foot-head">&nbsp;</div>
    <ul class="foot-list"><li>Career</li><li>Customer Care</li><li>FAQs</li><li>Gallery</li><li>Contact Us</li></ul>
  </div>
  <div class="abs" style="left:876px;top:57px">
    <div class="foot-head">CONNECT WITH US</div>
    <div class="social"><span></span><span></span><span></span><span></span><span></span></div>
  </div>
</footer>

</body>
</html>
```